Stylish Design With Simple UI For Appointment Site

Note: Logo file now attached. Extra credit to anyone who offers basic HTML templates in the final deliverable, incorporating the individual components of the design (using DIVs and CSS).

There are two key requirements for this site:

1. It makes our site look like one of the most professional of its kind. We want to look the part;
2. It has a very simple, straight-forward user interface. We're nothing without being intuitive.

Our site will be used by other businesses to set up their own online booking systems.

Logo samples attached. The colour scheme is not yet set but two possible options are:

1. Dark (#323B3A) & Blue (#12B5D4) on White background
2. White & Yellow (#FEF102) on Grey (#3A3A3C) background

For inspiration, and an idea of what we like, take a look at quillbarn.com - it's very clear and eye-catching, although its pages are longer than we would like ours to be. Oh but we don't need a chimp! Instead of the section with the chimp in, we would like a changing image headline section on the home page, in the style of fellgarde.co.uk (with a less high image; we have attached one image which you may want to try out with this, but happy to see other ideas).

Any graphics included must be royalty free and free for commercial use. Fonts should be readily available and specified.

We would like to see the design applied to the following pages:

1. The main public home page (features header, login prompt, menu, changing image banner with headlines, main body, footer menu).
2. A secondary public page (features a similar layout to home page but without image headline banner, includes extra panels/body detail).
3. The Control Panel page (features several list panels and an add appointment button).
4. A list-style administration page (with popup item editor window).
5. A settings administration page (with form).

In that order, a sample walk-through design spec will be attached.

To summarise, we are looking for someone to put forward not only a design but something which also focuses on the user interface. The designer should consider all of the examples and guidance given, but shouldn't let that limit any innovation.

Happy to respond to any questions and give constant feedback.

Thank you.

-*-*-*-*-*-*-*-*-*-*-*-*-*-*-*-*-

Update, 18th Nov 2011:

1. I'm about the upload the logos so you can incorporate these into your designs.

2. A UI question of mine is how to move from a list view (e.g. Resources) to editing one of those items in the list. In the spec document I showed a popup editor for these items but I don't know if that's the best thing to do. Happy to see other ideas on this - whatever the best user experience would be.

3. On the designs in the spec document I've not included any help functionality. It would be good to include pieces of guidance on each page of the administration area to help the user - guess these could either be info panels on the pages themselves or info popups. Again, would be good to see some ideas in the designs.

Also, just to be clear, I am really looking for something that looks like a modern innovative "web app" rather than it looking like a promotional corporate web site.

Target Market(s)

Owners of businesses of all types (e.g. salons, small hotels, surgeries, etc).

Industry/Entity Type

Commercial

Requirements
Must have
• Headline image transition panel on home page.

Layout, graphic and font styles along similar lines to quillbarn.com, fellgarde.co.uk, etc.
Nice to have
• Blog feed panel on the home page.

Innovative ideas for improvements to the spec.
Should not have
• Anything which can't be practically rendered when the design is converted to HTML.

Should not be overly influenced by the layout and style in the attached spec - that should just be a guide to the content and layout of the site.

```html
<!DOCTYPE html>
<html lang="en">
<head>
<meta charset="utf-8">
<title>Slotwise – Home</title>
<link rel="stylesheet" href="https://fonts.googleapis.com/css2?family=Source+Sans+3:wght@300;400;600&family=Petit+Formal+Script&display=swap">
<style>
  :root {
    --yellow: #fbe928;
    --yellow-deep: #e9cf12;
    --yellow-soft: #fdf38a;
    --grey: #343434;
    --grey-line: #4a4a4a;
    --grey-light: #5a5a5a;
    --white: #ffffff;
    --text-light: #f2f2f2;
    --caption-bg: rgba(0, 0, 0, 0.82);
  }
  * { box-sizing: border-box; margin: 0; padding: 0; }
  html, body { width: 1200px; height: 972px; overflow: hidden; }
  body {
    position: relative;
    font-family: "Source Sans 3", Arial, sans-serif;
    background: var(--white);
    color: var(--text-light);
  }
  .top-wash {
    position: absolute; left: 0; top: 0; width: 1200px; height: 300px;
    background: linear-gradient(180deg, var(--yellow) 0%, var(--yellow) 76%, #fdf6a0 84%, var(--white) 100%);
  }
  .lower-field {
    position: absolute; left: 0; top: 576px; width: 1200px; height: 396px;
    background: var(--grey);
  }

  /* language selector */
  .language { position: absolute; left: 47px; top: 8px; display: flex; align-items: center; gap: 10px; color: #222; font-size: 17px; }
  .language-select {
    width: 219px; height: 27px; background: var(--white); border-radius: 6px;
    display: flex; align-items: center; justify-content: space-between; padding: 0 12px;
    color: #8a8a8a; font-size: 16px;
  }

  /* brand panel */
  .brand-panel {
    position: absolute; left: 0; top: 46px; width: 464px; height: 184px;
    background: var(--grey); border-top-right-radius: 14px;
    display: flex; align-items: center; justify-content: center; gap: 16px;
  }
  .brand-mark { width: 26px; height: 26px; background: var(--yellow); }
  .brand-name { font-size: 44px; font-weight: 300; letter-spacing: 8px; color: var(--white); text-transform: uppercase; }

  /* login */
  .login-panel {
    position: absolute; left: 890px; top: 0; width: 296px; height: 172px;
    background: rgba(214, 190, 20, 0.35); border-radius: 0 0 8px 8px;
  }
  .login-field {
    position: absolute; left: 39px; width: 221px; height: 29px;
    background: var(--white); border-radius: 7px; padding-left: 16px;
    font-size: 14px; line-height: 29px; color: #333;
  }
  .login-button {
    position: absolute; left: 116px; top: 110px; width: 84px; height: 27px; border-radius: 7px;
    background: linear-gradient(180deg, #fff46a, var(--yellow-deep));
    color: #222; font-size: 17px; text-align: center; line-height: 27px;
  }
  .forgot { position: absolute; left: 0; width: 296px; top: 143px; text-align: center; font-size: 13px; color: #111; }

  /* main nav */
  .main-nav { position: absolute; left: 464px; top: 184px; width: 736px; height: 46px; background: var(--grey); }
  .main-nav a {
    position: absolute; top: 0; height: 40px; line-height: 42px; text-align: center;
    color: var(--white); text-decoration: none; font-size: 19px;
  }
  .main-nav a.is-current {
    background: linear-gradient(180deg, var(--yellow-soft), var(--yellow-deep));
    color: #222; border-radius: 0 0 6px 6px;
  }

  /* headline banner */
  .banner {
    position: absolute; left: 36px; top: 262px; width: 1134px; height: 388px;
    border: 3px solid #e6e6e6; border-radius: 6px; overflow: hidden;
    background: var(--white);
  }
  .banner-image {
    position: absolute; inset: 0;
    background: linear-gradient(100deg, #3a3a3a 0%, #9a9a9a 18%, #d9d9d9 40%, #bdbdbd 60%, #5c5450 80%, #2a2624 100%);
  }
  .banner-caption {
    position: absolute; left: 609px; top: 45px; width: 525px; height: 268px;
    background: var(--caption-bg); padding: 20px 0 0 30px;
    font-family: "Petit Formal Script", cursive; color: var(--yellow);
    font-size: 19px; line-height: 36px; white-space: nowrap; overflow: hidden;
  }
  .signup-button {
    position: absolute; left: 673px; top: 283px; width: 212px; height: 47px; border-radius: 5px;
    background: linear-gradient(180deg, #fff56e, var(--yellow-deep));
    border: 2px solid #b89e08;
    font-family: "Petit Formal Script", cursive; font-size: 28px; color: #111;
    text-align: center; line-height: 43px; font-weight: 600;
  }
  .banner-dots { position: absolute; left: 928px; top: 358px; display: flex; gap: 10px; }
  .banner-dots span { width: 16px; height: 16px; border-radius: 50%; background: var(--yellow); }
  .banner-dots span.is-current { background: #c8c8c8; }

  /* content columns */
  .column { position: absolute; top: 680px; }
  .column h2 { font-weight: 300; font-size: 30px; color: var(--yellow); line-height: 1; }
  .column p { font-size: 15px; line-height: 29px; color: var(--text-light); }
  .column-intro { left: 49px; width: 530px; top: 686px; }
  .column-intro p { margin-top: 18px; }
  .column-news { left: 632px; width: 540px; top: 674px; }
  .column-news .post-date { margin-top: 18px; font-weight: 600; }
  .column-divider { position: absolute; left: 592px; top: 660px; width: 1px; height: 252px; background: var(--grey-line); }
  .more-button {
    position: absolute; height: 26px; border-radius: 7px; text-align: center;
    font-size: 14px; line-height: 24px;
  }
  .more-button-yellow { left: 484px; top: 874px; width: 84px; background: linear-gradient(180deg, #fff46a, var(--yellow-deep)); color: #222; border: 1px solid #9e8a08; }
  .more-button-light { left: 1045px; top: 870px; width: 86px; background: var(--grey); color: var(--white); border: 1px solid #e8e8e8; }

  /* footer */
  .site-footer {
    position: absolute; left: 0; top: 926px; width: 1200px; height: 46px;
    background: var(--grey); border-top: 2px solid var(--grey-light);
  }
  .footer-nav a { position: absolute; top: 10px; color: #e4e4e4; text-decoration: none; font-size: 18px; font-weight: 300; }
  .copyright { position: absolute; right: 44px; top: 14px; font-size: 13px; color: #e4e4e4; }
</style>
</head>
<body>
  <div class="top-wash"></div>
  <div class="lower-field"></div>

  <div class="language">
    <span>Language :</span>
    <div class="language-select">
      <span>United States : English</span>
      <svg width="14" height="10" viewBox="0 0 14 10"><path d="M0 0h14L7 10z" fill="#222"/></svg>
    </div>
  </div>

  <div class="brand-panel">
    <span class="brand-mark"></span>
    <span class="brand-name">Slotwise</span>
  </div>

  <div class="login-panel">
    <div class="login-field" style="top:29px">Username</div>
    <div class="login-field" style="top:66px">Password</div>
    <div class="login-button">Login</div>
    <div class="forgot">Forgot Password?</div>
  </div>

  <nav class="main-nav">
    <a class="is-current" href="#" style="left:250px;width:90px">Home</a>
    <a href="#" style="left:354px;width:90px">Features</a>
    <a href="#" style="left:481px;width:90px">Pricing</a>
    <a href="#" style="left:586px;width:120px">Contact Us</a>
  </nav>

  <section class="banner">
    <div class="banner-image" role="img" aria-label="Close-up photograph of a clock face with hands and numerals"></div>
    <div class="banner-caption">
      Lorem ipsum dolor sit amet, consectetur<br>
      adipisicing elit, sed do eiusmod tempor<br>
      incididunt ut labore et dolore magna<br>
      aliqua. Ut enim ad minim veniam, quis<br>
      nostrud exercitation ullamco laboris nisi<br>
      ut aliquip ex ea commodo
    </div>
    <div class="signup-button">Sign Up</div>
    <div class="banner-dots"><span></span><span></span><span></span><span class="is-current"></span></div>
  </section>

  <section class="column column-intro">
    <h2>Make yourself Available</h2>
    <p>On the other hand, we denounce with righteous indignation and dislike men who are so beguiled and demoralized by the charms of pleasure of the moment, so blinded by desire, that they cannot foresee the pain and trouble that are bound to ensue; and equal blame belongs to those who fail in their duty through weakness of will, which is the same as saying through</p>
  </section>
  <div class="more-button more-button-yellow">more...</div>

  <div class="column-divider"></div>

  <section class="column column-news">
    <h2>What’s Happening</h2>
    <p class="post-date">1 Aug 2011</p>
    <p>Lorem ipsum dolor sit amet, consectetur adipisicing elit, sed do eiusmod tempor incididunt ut labore et dolore magna aliqua. Ut enim ad minim veniam, quis nostrud exercitation ullamco laboris nisi ut aliquip ex ea commodo consequat. Duis aute irure dolor in reprehenderit in voluptate velit esse</p>
  </section>
  <div class="more-button more-button-light">more...</div>

  <footer class="site-footer">
    <nav class="footer-nav">
      <a href="#" style="left:47px">Home</a>
      <a href="#" style="left:133px">Features</a>
      <a href="#" style="left:244px">Pricing</a>
      <a href="#" style="left:338px">Contact Us</a>
    </nav>
    <div class="copyright">Copyright © 2011. www.slotwise.com</div>
  </footer>
</body>
</html>
```